Rancho Verbena Wine Bottle Label

Hello! We are looking for a wine bottle label design for our private, family winery located in Chico, CA. The name of our home/ranch/vineyard is Rancho Verbena ('the exit'), which is inspired by our hilltop location, panoramic views of the valley, and sensation of escaping from the busy world below.

We planted our vineyard in 2011 and are now bottling our first harvest from fall of 2013. We planted all Italian varietals on our land: syrah, primitivo, and montepulciano. The wine we make is the culmination of all the love, support and effort poured into the process by our family and friends.

The task at hand: we are looking for a clean, simple front and back wine label design.

Front Label Content:
RV and/or Rancho Verbena
Estate Grown
Chico, CA
Varietal (use Syrah for placeholder)
Year (use 2013 for placeholder)

Back Label Content:
Running list of names of all family and friends who have participated in the process (use a text fill for placeholder)

Aesthetic Description:
Simple, clean, contemporary, text based design (see attached logo idea, Image #1)
Like the brown paper with stamped lettering look & feel
Like the classic clear label with gold lettering look & feel
Option to incorporated a simple background image/sketch of the view overlooking the valley (see attached Image #2 and #3)
Additional inspirational images attached for reference (Images #3- )

General Size Requirement:
Front Label - 4"tall by 3 1/2" wide
Back Label - 4"tall by 3 1/2" wide

Format:
Please submit Photoshop or Illustrator or InDesign Files and PDF/EPS Files.

```html
<!DOCTYPE html>
<html lang="en">
<head>
<meta charset="utf-8">
<title>Rancho Verbena – Syrah Label Set</title>
<link href="https://fonts.googleapis.com/css2?family=Josefin+Sans:wght@400&display=swap" rel="stylesheet">
<style>
  :root {
    --cream: #f3efe6;
    --stripe: rgba(150, 143, 132, 0.45);
    --kraft: #b48e70;
    --kraft-dark: #a07d62;
    --wine: #7a1014;
    --wine-soft: #8c1a1c;
  }
  * { margin: 0; padding: 0; box-sizing: border-box; }
  html, body { width: 1200px; height: 848px; overflow: hidden; }
  body {
    position: relative;
    background: var(--cream);
    font-family: "Josefin Sans", sans-serif;
    font-weight: 400;
  }
  .stripes {
    position: absolute; inset: 0;
    background: repeating-linear-gradient(150deg, transparent 0 24px, var(--stripe) 24px 56px);
    pointer-events: none;
    z-index: 2;
  }
  .label {
    position: absolute;
    top: 198px;
    width: 359px;
    height: 410px;
    background: linear-gradient(180deg, var(--kraft), var(--kraft-dark));
    color: var(--wine);
    z-index: 1;
  }
  .label--one { left: 35px; }
  .label--two { left: 418px; }
  .label--three { left: 809px; }
  .label__frame {
    position: absolute;
    inset: 10px 12px 10px 12px;
    border: 3px solid var(--wine);
  }
  .label__rule {
    position: absolute;
    top: 62px; left: 62px;
    width: 232px; height: 3px;
    background: var(--wine-soft);
  }
  .label__monogram {
    position: absolute;
    top: 96px; left: 0; width: 100%;
    text-align: center;
    font-size: 160px;
    line-height: 1;
    letter-spacing: -6px;
  }
  .label__vintage {
    position: absolute;
    top: 283px; left: 0; width: 100%;
    text-align: center;
    font-size: 25px;
  }
  .label__varietal {
    position: absolute;
    top: 333px; left: 0; width: 100%;
    text-align: center;
    font-size: 25px;
  }
  .label__estate {
    position: absolute;
    top: 380px; left: 0; width: 100%;
    text-align: center;
    font-size: 11px;
    letter-spacing: 0.2px;
  }
</style>
</head>
<body>
  <section class="label label--one">
    <div class="label__frame"></div>
    <div class="label__rule"></div>
    <div class="label__monogram">RV</div>
    <div class="label__vintage">2013</div>
    <div class="label__varietal">SYRAH</div>
    <div class="label__estate">RANCHO VERBENA - ESTATE GROWN - CHICO, CA</div>
  </section>

  <section class="label label--two">
    <div class="label__frame"></div>
    <div class="label__rule"></div>
    <div class="label__monogram">RV</div>
    <div class="label__vintage">2013</div>
    <div class="label__varietal">SYRAH</div>
    <div class="label__estate">RANCHO VERBENA - ESTATE GROWN - CHICO, CA</div>
  </section>

  <section class="label label--three">
    <div class="label__frame"></div>
    <div class="label__rule"></div>
    <div class="label__monogram">RV</div>
    <div class="label__vintage">2013</div>
    <div class="label__varietal">SYRAH</div>
    <div class="label__estate">RANCHO VERBENA - ESTATE GROWN - CHICO, CA</div>
  </section>

  <div class="stripes"></div>
</body>
</html>
```